Marketing Thornbury

We are a primary school and would like to market our school in a positive light. We have had recent success and would like the local community to know!

Target Market(s)

Parents/Carers in the local community

Industry/Entity Type

School

Font styles to use
Serif

Requirements
Must have
• Thornbury Logo first with our moto 'Growing Bright Minds'

Reference to the fact we are converting to academy status on 1st April 2014 with The Harwick BRIDGE Academy Trust

Reference to the partnership with Colsworth Primary School which has bought recent, quick success

Reference to Edrevue rating of Good. Feb 2014
Nice to have
• School colours dark red

Link to website www.thornburyprimary.example

Link to the academy website www.harwickbridge.example

Statements from Edrevue -

'This is a good school'

'The Executive Headteacher and leadership team have skilfully steered the school's recovery and galvanised staff at all levels to work as a team'

'This is a very different school to the one that existed at the time of the previous inspection'

'Pupils achievement has improved very quickly this year'

'Pupils make a strong start in the school'

'The quality of teaching is good'

'The behaviour of pupils is good'

```html
<!DOCTYPE html>
<html lang="en">
<head>
<meta charset="utf-8">
<title>Thornbury School – Admission Flyer</title>
<link rel="stylesheet" href="https://fonts.googleapis.com/css2?family=Open+Sans:wght@400;600;700;800&display=swap">
<style>
  :root {
    --page-bg: #ebe5ee;
    --maroon: #4b0d0f;
    --ring-brown: #7b3d22;
    --ring-tan: #b07a5c;
    --gold: #c9a24a;
    --orange: #ee7d2b;
    --white: #ffffff;
    --cream: #f4ebe4;
    --star: #f5b51c;
    --photo-a: #d9c6b8;
    --photo-b: #8fb4d8;
  }
  * { margin: 0; padding: 0; box-sizing: border-box; }
  html, body {
    width: 1200px; height: 750px; overflow: hidden;
    background: var(--page-bg);
    font-family: "Open Sans", Arial, sans-serif;
  }
  .flyer {
    position: absolute; left: 348px; top: 25px;
    width: 503px; height: 700px;
    background: var(--maroon);
    overflow: hidden;
    color: var(--white);
  }
  .flyer-shapes { position: absolute; inset: 0; }
  .badge {
    position: absolute; left: 15px; top: 8px; width: 78px; height: 78px;
    display: flex; align-items: center; justify-content: center; text-align: center;
    font-weight: 700; font-size: 11.5px; line-height: 1.15; color: var(--white);
  }
  .headline {
    position: absolute; left: 160px; top: 45px; width: 340px; text-align: center;
    font-weight: 800; font-size: 32px; line-height: 1.12; color: var(--orange);
    -webkit-text-stroke: 1.2px var(--white); paint-order: stroke fill;
  }
  .subtitle {
    position: absolute; right: 181px; top: 130px; width: 240px; text-align: right;
    font-size: 16px; line-height: 1.25; font-weight: 600;
  }
  .intro {
    position: absolute; right: 181px; top: 177px; width: 240px; text-align: right;
    font-size: 11.5px; line-height: 1.38;
  }
  .body-copy {
    position: absolute; left: 340px; top: 133px; width: 138px;
    font-size: 9.6px; line-height: 1.5; text-align: justify; color: var(--cream);
  }
  .body-copy p + p { margin-top: 4px; }
  .school-mark {
    position: absolute; left: 14px; top: 262px; width: 110px;
    display: flex; flex-direction: column; align-items: center; gap: 6px;
  }
  .school-mark .dot {
    width: 34px; height: 34px; border-radius: 50%; background: var(--gold);
  }
  .school-mark .name {
    font-weight: 700; font-size: 12px; letter-spacing: 1px; color: var(--gold); text-align: center;
  }
  .rating {
    position: absolute; right: 40px; top: 505px; text-align: right;
    font-size: 11px; line-height: 1.2; letter-spacing: .5px;
  }
  .rating .stars { color: var(--star); font-size: 12px; letter-spacing: 1px; }
  .trust {
    position: absolute; left: 288px; top: 552px; width: 190px; text-align: center;
  }
  .trust-name { font-size: 15px; line-height: 1.15; font-weight: 400; letter-spacing: .3px; }
  .trust-motto {
    margin-top: 6px; padding-top: 4px; border-top: 1.5px solid var(--white);
    font-size: 11px; font-weight: 700; letter-spacing: .6px;
  }
  .contacts {
    position: absolute; left: 308px; top: 620px; list-style: none;
    font-size: 10.5px; line-height: 1.35;
  }
  .contacts li { display: flex; align-items: flex-start; gap: 7px; margin-bottom: 4px; }
  .contacts svg { flex: none; margin-top: 1px; }
</style>
</head>
<body>
<main class="flyer">
  <svg class="flyer-shapes" width="503" height="700" viewBox="0 0 503 700" aria-hidden="true">
    <g fill="none" stroke="var(--ring-tan)" opacity=".55">
      <circle cx="54" cy="47" r="52" stroke-width="7"/>
      <circle cx="160" cy="12" r="13" stroke-width="4"/>
      <circle cx="220" cy="98" r="8" stroke-width="3"/>
      <circle cx="124" cy="120" r="17" stroke-width="4"/>
      <circle cx="40" cy="166" r="20" stroke-width="5"/>
      <circle cx="64" cy="214" r="12" stroke-width="3"/>
      <circle cx="296" cy="262" r="22" stroke-width="5"/>
      <circle cx="440" cy="388" r="12" stroke-width="3"/>
    </g>
    <g fill="var(--ring-tan)" opacity=".35">
      <circle cx="124" cy="120" r="10"/>
      <circle cx="40" cy="166" r="12"/>
      <circle cx="296" cy="262" r="13"/>
    </g>
    <circle cx="54" cy="47" r="39" fill="var(--gold)"/>
    <circle cx="138" cy="538" r="145" fill="var(--ring-brown)"/>
    <circle cx="138" cy="538" r="124" fill="var(--ring-tan)" opacity=".45"/>
    <circle cx="199" cy="320" r="76" fill="var(--ring-brown)"/>
    <circle cx="340" cy="409" r="86" fill="var(--ring-brown)"/>
    <defs>
      <radialGradient id="photoWarm" cx=".5" cy=".45" r=".6">
        <stop offset="0" stop-color="var(--photo-a)"/>
        <stop offset="1" stop-color="#f6f1ee"/>
      </radialGradient>
      <linearGradient id="photoSky" x1="0" y1="0" x2="0" y2="1">
        <stop offset="0" stop-color="var(--photo-b)"/>
        <stop offset="1" stop-color="#d4a98a"/>
      </linearGradient>
    </defs>
    <circle cx="199" cy="320" r="55" fill="url(#photoSky)" role="img" aria-label="Photo of smiling pupils pointing upwards"/>
    <circle cx="340" cy="409" r="64" fill="url(#photoSky)" role="img" aria-label="Photo of a group of happy children outdoors"/>
    <circle cx="138" cy="538" r="117" fill="url(#photoWarm)" role="img" aria-label="Photo of children in a circle joining hands"/>
  </svg>

  <div class="badge">Hurry-up!<br>ADMISSION<br>OPEN</div>

  <h1 class="headline">Growing Bright<br>Minds</h1>

  <p class="subtitle">Rated Good by Edrevue<br>February 2014</p>
  <p class="intro">We're open to all children aged 3 to 5.<br>'Pupils make a strong start in the school.'<br>'The quality of teaching is good.'<br>'The behaviour of pupils is good.'</p>

  <div class="body-copy">
    <p>On 1st April 2014 Thornbury converts to academy status with The Harwick BRIDGE Academy Trust, joining a family of schools that puts every child first.</p>
    <p>Our partnership with Colsworth Primary School has brought recent, quick success. 'Pupils achievement has improved very quickly this year.' – Edrevue</p>
  </div>

  <div class="school-mark">
    <span class="dot"></span>
    <span class="name">THORNBURY SCHOOL</span>
  </div>

  <div class="rating">
    PARENT RATING<br>
    <span class="stars">★★★★★</span><br>
    2010 ~ 2014
  </div>

  <div class="trust">
    <div class="trust-name">HARWICK BRIDGE<br>ACADEMY TRUST</div>
    <div class="trust-motto">GROWING BRIGHT MINDS</div>
  </div>

  <ul class="contacts">
    <li>
      <svg width="10" height="13" viewBox="0 0 10 13"><path d="M5 0a5 5 0 0 1 5 5c0 3.5-5 8-5 8S0 8.5 0 5a5 5 0 0 1 5-5z" fill="var(--white)"/><circle cx="5" cy="5" r="1.8" fill="var(--maroon)"/></svg>
      <span>14 Orchard Lane,<br>Thornbury TB4 7EL</span>
    </li>
    <li>
      <svg width="11" height="11" viewBox="0 0 12 12" fill="none" stroke="var(--white)" stroke-width="1.2"><circle cx="6" cy="6" r="5.2"/><ellipse cx="6" cy="6" rx="2.2" ry="5.2"/><path d="M.8 6h10.4"/></svg>
      <span>www.harwickbridge.example</span>
    </li>
    <li>
      <svg width="11" height="11" viewBox="0 0 12 12" fill="none" stroke="var(--white)" stroke-width="1.2"><circle cx="6" cy="6" r="5.2"/><ellipse cx="6" cy="6" rx="2.2" ry="5.2"/><path d="M.8 6h10.4"/></svg>
      <span>www.thornburyprimary.example</span>
    </li>
  </ul>
</main>
</body>
</html>
```